Obrelo Business Card

Need a double sided business card. Would like the business card to have the logo on one side and the employees details and business contact details on the other.

Business

```html
<!DOCTYPE html>
<html lang="en">
<head>
<meta charset="utf-8">
<title>Obrelo Business Card</title>
<link rel="stylesheet" href="https://fonts.googleapis.com/css2?family=Lato:wght@300;400;700;900&display=swap">
<style>
  :root {
    --page: #d6d0c6;
    --card-dark: #1c1c1c;
    --card-mid: #2a2a2a;
    --card-band: #363636;
    --card-band-light: #444444;
    --accent: #e0302f;
    --accent-soft: #f05a5a;
    --ink: #ffffff;
    --ink-muted: #d8d8d8;
  }
  * { box-sizing: border-box; margin: 0; padding: 0; }
  html, body {
    width: 1200px; height: 913px; overflow: hidden;
    background: var(--page);
    font-family: "Lato", sans-serif;
  }
  .canvas { position: relative; width: 1200px; height: 913px; }

  .card {
    position: absolute;
    width: 540px; height: 309px;
    overflow: hidden;
    border-radius: 3px;
    box-shadow: 0 14px 30px rgba(0,0,0,0.28);
    background: linear-gradient(180deg, var(--card-mid) 0%, var(--card-dark) 100%);
  }
  .card--front { left: 60px; top: 110px; }
  .card--back { left: 600px; top: 490px; }

  /* front */
  .front__band {
    position: absolute; left: 0; right: 0;
    background: linear-gradient(180deg, var(--card-band-light), var(--card-band));
  }
  .front__band--upper { top: 62px; height: 70px; opacity: .55; }
  .front__band--main { top: 132px; height: 92px; }
  .front__bar {
    position: absolute; height: 9px; background: var(--accent);
  }
  .front__bar--top { top: 0; left: 150px; width: 250px; background: var(--accent-soft); }
  .front__bar--bottom { bottom: 0; right: 120px; width: 250px; }
  .front__brand {
    position: absolute; left: 200px; top: 148px;
    text-align: right; color: var(--ink);
  }
  .brand-name {
    font-size: 34px; font-weight: 900; letter-spacing: .5px; line-height: 1;
    text-transform: uppercase;
  }
  .brand-slogan {
    font-size: 17px; font-weight: 300; color: var(--ink-muted); margin-top: 4px;
  }

  /* back */
  .back__head {
    position: absolute; left: 0; right: 0; top: 0; height: 62px;
    background: var(--card-dark);
  }
  .back__panel {
    position: absolute; left: 0; right: 0; top: 62px; height: 196px;
    background: linear-gradient(180deg, #3a3a3a, #2c2c2c);
  }
  .back__foot {
    position: absolute; left: 0; right: 0; bottom: 0; height: 51px;
    background: var(--card-dark);
  }
  .person {
    position: absolute; right: 26px; top: 14px; text-align: right; color: var(--ink);
  }
  .person__name { font-size: 17px; font-weight: 900; text-transform: uppercase; letter-spacing: .3px; }
  .person__role { font-size: 9px; font-weight: 400; text-transform: uppercase; color: var(--ink-muted); letter-spacing: .6px; }

  .contact-icons {
    position: absolute; left: 34px; top: 80px; width: 38px; height: 176px;
    background: var(--accent);
    display: flex; flex-direction: column; justify-content: space-around; align-items: center;
  }
  .contact-icons svg { width: 18px; height: 18px; fill: var(--ink); }
  .contact-list {
    position: absolute; left: 88px; top: 80px; height: 176px;
    list-style: none;
    display: flex; flex-direction: column; justify-content: space-around;
    color: var(--ink); font-size: 16px; font-weight: 400;
  }
</style>
</head>
<body>
<main class="canvas">

  <section class="card card--front" aria-label="Card front">
    <div class="front__band front__band--upper"></div>
    <div class="front__band front__band--main"></div>
    <div class="front__bar front__bar--top"></div>
    <div class="front__bar front__bar--bottom"></div>
    <div class="front__brand">
      <p class="brand-name">Obrelo</p>
      <p class="brand-slogan">your slogan here</p>
    </div>
  </section>

  <section class="card card--back" aria-label="Card back">
    <div class="back__head"></div>
    <div class="back__panel"></div>
    <div class="back__foot"></div>
    <div class="person">
      <p class="person__name">Marten Lovik</p>
      <p class="person__role">Art Director</p>
    </div>
    <div class="contact-icons" aria-hidden="true">
      <svg viewBox="0 0 24 24"><path d="M6.6 10.8a15 15 0 0 0 6.6 6.6l2.2-2.2c.3-.3.7-.4 1-.2 1.1.4 2.3.6 3.6.6.6 0 1 .4 1 1V20c0 .6-.4 1-1 1A17 17 0 0 1 3 4c0-.6.4-1 1-1h3.5c.6 0 1 .4 1 1 0 1.2.2 2.4.6 3.6.1.3 0 .7-.2 1z"/></svg>
      <svg viewBox="0 0 24 24"><path d="M7 2h10a2 2 0 0 1 2 2v16a2 2 0 0 1-2 2H7a2 2 0 0 1-2-2V4a2 2 0 0 1 2-2zm0 3v13h10V5zm5 14.2a1 1 0 1 0 0 .1z"/></svg>
      <svg viewBox="0 0 24 24"><path d="M2 5h20v14H2zm2 2v.4l8 5.3 8-5.3V7zm0 2.8V17h16V9.8l-8 5.3z"/></svg>
      <svg viewBox="0 0 24 24"><path d="M12 2a10 10 0 1 0 0 20 10 10 0 0 0 0-20zm-1 17.9A8 8 0 0 1 4.1 11H7c.1 2.9.9 5.9 2.2 7.9zM4.1 9A8 8 0 0 1 11 4.1V9zm8.9 10.9V13h3.9a8 8 0 0 1-3.9 6.9zM13 11V4.1A8 8 0 0 1 19.9 11z"/></svg>
      <svg viewBox="0 0 24 24"><path d="M12 2a7 7 0 0 0-7 7c0 5.2 7 13 7 13s7-7.8 7-13a7 7 0 0 0-7-7zm0 9.5a2.5 2.5 0 1 1 0-5 2.5 2.5 0 0 1 0 5z"/></svg>
    </div>
    <ul class="contact-list">
      <li>+2 (4820) 6613097</li>
      <li>+2 (4820) 6613098</li>
      <li>hello@obrelo.com</li>
      <li>www.obrelo.com</li>
      <li>3187 Harlow St, Ave Weston, New York</li>
    </ul>
  </section>

</main>
</body>
</html>
```